Fernvale Business Card Design

We are looking for a fresh business card design for our new logo. We would like a business card that is unique but friendly. We are in the window coverings business offering blinds, shutters and shades for homes.

Target Market(s)

Targeting the end-consumer

Industry/Entity Type

Business

Requirements
Must have
• Must have a dedicates space for a photo of our sales person. Must contain our new logo (attached).

```html
<!DOCTYPE html>
<html lang="en">
<head>
<meta charset="utf-8">
<title>Fernvale Business Card</title>
<link href="https://fonts.googleapis.com/css2?family=Questrial&display=swap" rel="stylesheet">
<style>
  :root {
    --stage: #4b4e53;
    --leaf-green: #8bc43f;
    --ink: #1b1b1b;
    --paper-white: #ffffff;
    --mark-grey: #6f7073;
    --photo-tone: #2a2a2a;
  }
  * { margin: 0; padding: 0; box-sizing: border-box; }
  html, body { width: 1200px; height: 1000px; overflow: hidden; }
  body {
    background: var(--stage);
    font-family: "Questrial", "Century Gothic", sans-serif;
    position: relative;
  }
  .card {
    position: absolute;
    left: 204px;
    width: 791px;
    background: var(--leaf-green);
    overflow: hidden;
    box-shadow: 0 6px 14px rgba(0,0,0,0.35);
  }
  .card-front { top: 34px; height: 451px; }
  .card-back { top: 510px; height: 450px; }

  /* Front */
  .portrait-slot {
    position: absolute; left: 0; top: 116px;
    width: 219px; height: 218px;
    background: linear-gradient(180deg, var(--ink), var(--photo-tone));
  }
  .holder-name {
    position: absolute; left: 241px; top: 106px;
    color: var(--paper-white); font-size: 58px; line-height: 1; letter-spacing: 0.5px;
  }
  .holder-role {
    position: absolute; left: 241px; top: 168px;
    color: var(--paper-white); font-size: 29px; line-height: 1; letter-spacing: 1px;
  }
  .name-rule {
    position: absolute; left: 241px; top: 211px;
    width: 444px; height: 2px; background: var(--ink);
  }
  .icon-rail {
    position: absolute; left: 242px; top: 212px;
    width: 31px; height: 122px; background: var(--ink);
  }
  .icon-rail svg { position: absolute; left: 6px; width: 19px; height: 19px; }
  .contact-list { list-style: none; position: absolute; left: 286px; top: 233px; }
  .contact-list li {
    color: var(--paper-white); font-size: 20px; line-height: 36px; height: 36px;
  }
  .front-band {
    position: absolute; left: 0; bottom: 0;
    width: 100%; height: 55px; background: var(--ink);
  }
  .brand-small {
    position: absolute; right: 33px; top: 13px;
    display: flex; align-items: center; gap: 10px;
  }
  .brand-small .brand-square { width: 28px; height: 28px; background: var(--mark-grey); }
  .brand-small .brand-name { color: var(--mark-grey); font-size: 25px; }

  /* Back */
  .back-band {
    position: absolute; left: 0; top: 138px;
    width: 100%; height: 172px; background: var(--ink);
  }
  .brand-large {
    position: absolute; left: 93px; top: 20px;
    display: flex; align-items: center; gap: 28px;
  }
  .brand-large .brand-square { width: 132px; height: 132px; background: var(--mark-grey); }
  .brand-large .brand-name { color: var(--mark-grey); font-size: 96px; line-height: 1; }
  .back-web {
    position: absolute; left: 0; width: 100%; top: 411px;
    text-align: center; color: var(--ink); font-size: 18px;
  }
</style>
</head>
<body>
  <section class="card card-front">
    <div class="portrait-slot" role="img" aria-label="Photo of the sales associate"></div>
    <h1 class="holder-name">DANA REYES</h1>
    <p class="holder-role">SALES ASSOCIATE</p>
    <div class="name-rule"></div>
    <div class="icon-rail">
      <svg style="top:24px" viewBox="0 0 20 20" aria-hidden="true">
        <path d="M5 2 L8 2 L9 6 L7 8 C8 11 9 12 12 13 L14 11 L18 12 L18 15 C18 17 16 18 14 18 C8 17 3 12 2 6 C2 4 3 2 5 2 Z" fill="var(--leaf-green)"/>
      </svg>
      <svg style="top:60px" viewBox="0 0 20 20" aria-hidden="true" fill="none" stroke="var(--leaf-green)" stroke-width="1.6">
        <circle cx="10" cy="10" r="8"/>
        <ellipse cx="10" cy="10" rx="3.5" ry="8"/>
        <line x1="2" y1="10" x2="18" y2="10"/>
        <line x1="3.5" y1="6" x2="16.5" y2="6"/>
        <line x1="3.5" y1="14" x2="16.5" y2="14"/>
      </svg>
      <svg style="top:96px" viewBox="0 0 20 20" aria-hidden="true">
        <rect x="1" y="4" width="18" height="12" fill="var(--leaf-green)"/>
        <path d="M1 4 L10 11 L19 4" fill="none" stroke="var(--ink)" stroke-width="1.4"/>
      </svg>
    </div>
    <ul class="contact-list">
      <li>+123.555.0142</li>
      <li>www.fernvaleshutters.com</li>
      <li>dana.reyes@fernvaleshutters.com</li>
    </ul>
    <div class="front-band">
      <div class="brand-small">
        <span class="brand-square"></span>
        <span class="brand-name">Fernvale</span>
      </div>
    </div>
  </section>

  <section class="card card-back">
    <div class="back-band">
      <div class="brand-large">
        <span class="brand-square"></span>
        <span class="brand-name">Fernvale</span>
      </div>
    </div>
    <p class="back-web">www.fernvaleshutters.com</p>
  </section>
</body>
</html>
```